Marlowe Restoration & Remodeling Group LLC

Roofing, windows, gutters services offered.
0% 6 months interest free financing
Vernon windows
Whitfield windows
KTR roofing shingles
ULP roofing shingles
Offering 30-50 year warranties.
Accepting all major credit cards, checks
Emergency services available

Target Market(s)

Roofing contractors

Industry/Entity Type

Roofing

Number of Pages Required

3 page

Font styles to use
Sans Serif

Requirements
Must have
• MUST HAVE SEO all necessary codes!!!!!!!!!!
• also I want button for "schedule appointment" so I can receive notification of an appointment, and also need live calendar integrated in that button
Nice to have
• Modern, professional site

```html
<!DOCTYPE html>
<html lang="en">
<head>
<meta charset="utf-8">
<title>Marlowe Restoration &amp; Remodeling Group LLC | Roofing, Windows &amp; Gutters</title>
<meta name="description" content="Marlowe Restoration & Remodeling Group LLC – roofing, windows and gutters. Vernon and Whitfield windows, KTR and ULP roofing shingles. 0% 6 months interest free financing, 30-50 year warranties, emergency services.">
<meta name="keywords" content="roofing contractor, windows, gutters, Vernon windows, Whitfield windows, KTR shingles, ULP shingles, remodeling">
<meta name="robots" content="index, follow">
<link rel="canonical" href="https://example.com/">
<meta property="og:title" content="Marlowe Restoration & Remodeling Group LLC">
<meta property="og:description" content="Roofing, windows and gutters with 0% 6 months interest free financing.">
<meta property="og:type" content="website">
<meta name="viewport" content="width=1200">
<link href="https://fonts.googleapis.com/css2?family=Quicksand:wght@400;500;600&family=Open+Sans:wght@400;600&display=swap" rel="stylesheet">
<style>
:root{
  --blue:#2697d9;
  --blue-light:#3aa9e6;
  --dark:#2b2b2b;
  --ink:#333;
  --grey:#dcdcdc;
  --faq-grey:#d9d9d9;
  --answer:#f1f1f1;
  --white:#fff;
}
*{margin:0;padding:0;box-sizing:border-box}
html,body{width:1200px;height:4219px;overflow:hidden}
body{position:relative;background:var(--white);font-family:"Open Sans",Arial,sans-serif;color:var(--ink)}
.abs{position:absolute}
.heading{font-family:"Quicksand",Arial,sans-serif;font-weight:500;text-align:center;width:100%;left:0}
.btn{position:absolute;display:flex;align-items:center;justify-content:center;font-size:11px;color:var(--white);background:var(--blue);text-decoration:none;letter-spacing:.3px}
.btn--dark{background:#1f1f1f}

/* header */
.site-header{top:0;left:0;width:1200px;height:123px;background:var(--white)}
.brand{left:152px;top:22px;display:flex;align-items:center;gap:10px;text-decoration:none}
.brand__mark{width:50px;height:50px;background:var(--blue)}
.brand__name{font-family:"Quicksand",sans-serif;font-weight:500;font-size:16px;color:var(--blue);line-height:1.2;width:180px}
.phone{left:912px;top:20px;font-family:"Quicksand",sans-serif;font-weight:600;font-size:18px;color:#222;display:flex;align-items:center;gap:8px}
.schedule-btn{left:736px;top:18px;width:158px;height:28px;font-size:11px;font-weight:600;gap:6px}
.nav{top:84px;left:0;width:1200px;height:20px}
.nav a{position:absolute;transform:translateX(-50%);font-size:11.5px;color:#555;text-decoration:none;white-space:nowrap}
.nav a.active{color:var(--blue)}

/* hero */
.hero{top:123px;left:0;width:1200px;height:620px;background:linear-gradient(180deg,#3d7ad0 0%,#8fb3dd 35%,#d9d4cb 55%,#8c8478 75%,#4b6b34 100%)}
.hero__arrow{top:345px;width:39px;height:40px;background:var(--blue);display:flex;align-items:center;justify-content:center}

.welcome__title{top:755px;font-size:33px;color:var(--blue)}
.welcome__text{top:804px;left:147px;width:906px;text-align:center;font-size:12px;line-height:21px;color:#444}

/* services */
.services__title{top:1116px;font-size:32px;color:var(--white)}
.service-card{top:1172px;height:246px}
.service-card__photo{height:190px}
.service-card__label{height:56px;background:var(--dark);color:var(--white);font-family:"Quicksand",sans-serif;font-size:25px;display:flex;align-items:center;justify-content:center}
.services__brands{top:1440px;left:0;width:100%;text-align:center;font-family:"Quicksand",sans-serif;font-weight:500;font-size:16px;color:var(--white)}

/* testimonials */
.testimonials__title{top:1620px;font-size:32px;color:var(--blue)}
.testimonial__quote{top:1675px;left:150px;width:900px;text-align:center;font-size:15px;line-height:25px;color:#444}
.testimonial__name{top:1728px;font-family:"Quicksand",sans-serif;font-weight:600;font-size:19px;text-align:center;width:100%;color:#222}
.testimonial__stars{top:1756px;left:0;width:100%;text-align:center;color:var(--blue);font-size:13px;letter-spacing:2px}

/* financing */
.finance__big{top:1935px;font-family:"Quicksand",sans-serif;font-weight:600;font-size:92px;color:var(--white);text-align:center;width:100%}
.finance__sub{top:2033px;font-size:32px;color:var(--white)}

/* faq */
.faq__title{top:2337px;font-size:32px;color:var(--blue)}
.faq__item{left:144px;width:912px;height:47px;background:var(--faq-grey);font-family:"Quicksand",sans-serif;font-weight:500;font-size:15.5px;color:#444;display:flex;align-items:center;justify-content:space-between;padding:0 24px}
.faq__item--open{background:var(--blue);color:var(--white)}
.faq__answer{left:144px;top:2451px;width:912px;height:37px;background:var(--answer);font-size:11px;color:#555;display:flex;align-items:center;padding:0 24px}

/* gallery */
.gallery__title{top:3053px;font-size:32px;color:var(--blue)}

/* features */
.feature{top:3850px;width:320px;text-align:center;transform:translateX(-50%)}
.feature__text{margin-top:8px;font-family:"Quicksand",sans-serif;font-weight:500;font-size:20px;line-height:28px;color:#333}

/* footer */
.footer__social{top:4046px;left:0;width:1200px;height:50px}
.footer__links{top:4126px;left:0;width:100%;text-align:center;font-size:11.5px;color:#bbb}
.footer__links a{color:#bbb;text-decoration:none;margin:0 8px}
.footer__copy{top:4158px;left:0;width:100%;text-align:center;font-size:11.5px;color:#bbb}
</style>
</head>
<body>

<header class="abs site-header">
  <a class="abs brand" href="#">
    <span class="brand__mark"></span>
    <span class="brand__name">Marlowe Restoration &amp; Remodeling Group LLC</span>
  </a>
  <a class="btn schedule-btn" href="#schedule-appointment" title="Schedule an appointment – live calendar">
    <svg width="12" height="12" viewBox="0 0 24 24"><rect x="2" y="4" width="20" height="18" rx="2" fill="none" stroke="#fff" stroke-width="2.5"/><rect x="2" y="4" width="20" height="5" fill="#fff"/><rect x="6" y="1" width="2.5" height="5" fill="#fff"/><rect x="15.5" y="1" width="2.5" height="5" fill="#fff"/></svg>
    SCHEDULE APPOINTMENT
  </a>
  <div class="abs phone">
    <svg width="16" height="16" viewBox="0 0 24 24"><path fill="#222" d="M6.6 10.8a15.1 15.1 0 0 0 6.6 6.6l2.2-2.2c.3-.3.7-.4 1-.2 1.1.4 2.3.6 3.6.6.6 0 1 .4 1 1V20c0 .6-.4 1-1 1A17 17 0 0 1 3 4c0-.6.4-1 1-1h3.5c.6 0 1 .4 1 1 0 1.3.2 2.5.6 3.6.1.3 0 .7-.2 1z"/></svg>
    555 014 2287
  </div>
  <nav class="abs nav">
    <a class="active" href="#" style="left:553px">Home</a>
    <a href="#" style="left:627px">About Us</a>
    <a href="#" style="left:709px">Services</a>
    <a href="#" style="left:784px">Gallery</a>
    <a href="#" style="left:869px">Testimonials</a>
    <a href="#" style="left:948px">FAQ</a>
    <a href="#" style="left:1023px">Contact US</a>
  </nav>
</header>

<section class="abs hero" role="img" aria-label="Photo of a two-storey stucco house with tiled roof and double garage"></section>
<div class="abs hero__arrow" style="left:0"><svg width="14" height="20" viewBox="0 0 14 20"><path d="M11 2 3 10l8 8" stroke="#fff" stroke-width="3" fill="none"/></svg></div>
<div class="abs hero__arrow" style="left:1161px"><svg width="14" height="20" viewBox="0 0 14 20"><path d="M3 2l8 8-8 8" stroke="#fff" stroke-width="3" fill="none"/></svg></div>

<svg class="abs" style="top:0;left:0" width="1200" height="4219" viewBox="0 0 1200 4219">
  <polygon points="0,720 600,612 1200,728 1200,745 0,745" fill="var(--blue)"/>
  <polygon points="0,737 600,630 1200,740 1200,745 0,745" fill="#fff"/>
  <polygon points="0,1115 600,992 1200,1115 1200,1621 600,1493 0,1621" fill="var(--blue)"/>
</svg>

<h1 class="abs heading welcome__title">Welcome to Marlowe Restoration &amp; Remodeling Group, LLC</h1>
<p class="abs welcome__text">Maecenas tortor accumsan quam varius imperdiet vel eget elit. Aenean facilisis tincidunt lectus, id dictum nisi luctus eget. Vivamus efficitur ex condimentum, male suada eros eget, feugiat nibh. Sed tellus ex, imperdiet eget gravida sit amet, volutpat eget turpis. In nec ultricies est. Etiam mattis augue vehicula odio posuere, sit amet tempus lectus luctus. Nulla facilisi. Etiam vel massa elementum, bibendum tellus venenatis, feugiat massa.</p>
<a class="btn" href="#" style="left:552px;top:877px;width:96px;height:35px">READ MORE</a>

<h2 class="abs heading services__title">Services</h2>
<article class="abs service-card" style="left:144px;width:298px">
  <div class="service-card__photo" role="img" aria-label="House with new roofing" style="background:linear-gradient(180deg,#8fa6c4,#8a4a3a 45%,#d8cfb4 70%,#5f7a3c)"></div>
  <div class="service-card__label">Roofing</div>
</article>
<article class="abs service-card" style="left:452px;width:296px">
  <div class="service-card__photo" role="img" aria-label="Blue house with new windows" style="background:linear-gradient(180deg,#cfe0ef,#44556f 35%,#5b6f93 70%,#6c8a4b)"></div>
  <div class="service-card__label">Windows</div>
</article>
<article class="abs service-card" style="left:758px;width:298px">
  <div class="service-card__photo" role="img" aria-label="Roof edge with gutter installation" style="background:linear-gradient(120deg,#4f6b3a 0%,#7d8a6a 30%,#c09456 55%,#b8864a 100%)"></div>
  <div class="service-card__label">Gutters</div>
</article>
<p class="abs services__brands">Vernon &amp; Whitfield windows &nbsp;·&nbsp; KTR &amp; ULP roofing shingles</p>

<h2 class="abs heading testimonials__title">Testimonials</h2>
<svg class="abs" style="left:54px;top:1687px" width="16" height="24" viewBox="0 0 16 24"><path d="M13 2 3 12l10 10" stroke="#777" stroke-width="3" fill="none"/></svg>
<svg class="abs" style="left:1128px;top:1687px" width="16" height="24" viewBox="0 0 16 24"><path d="M3 2l10 10L3 22" stroke="#777" stroke-width="3" fill="none"/></svg>
<blockquote class="abs testimonial__quote">“ Excellent contractor. Easy to work with. Extremely recommended. We had roofing project and we were surprised by how Marlowe Restoration and remodeling care about there customers. Affordable and reliable. ”</blockquote>
<div class="abs testimonial__name">Daniel R</div>
<div class="abs testimonial__stars">★★★★★</div>

<svg class="abs" style="top:1838px;left:0" width="1200" height="505" viewBox="0 1838 1200 505" role="img" aria-label="Close-up of blue roof shingles against a cloudy sky">
  <defs>
    <linearGradient id="roofFill" x1="0" y1="0" x2="1" y2="1">
      <stop offset="0" stop-color="#5fb9ec"/>
      <stop offset=".5" stop-color="#2c95d6"/>
      <stop offset="1" stop-color="#1c78bd"/>
    </linearGradient>
  </defs>
  <polygon points="0,1964 600,1840 1200,1964 1200,2341 600,2213 0,2341" fill="url(#roofFill)"/>
</svg>
<div class="abs finance__big">0%</div>
<div class="abs heading finance__sub">6 months interest free financing</div>
<a class="btn btn--dark" href="#" style="left:552px;top:2081px;width:96px;height:34px">READ MORE</a>

<h2 class="abs heading faq__title">FAQ</h2>
<div class="abs faq__item faq__item--open" style="top:2402px">What should the customer know about your pricing (e.g., discounts, fees)?<svg width="12" height="8"><path d="M0 8 6 1l6 7z" fill="#fff"/></svg></div>
<div class="abs faq__answer">We provide all kind of ways to pay for project. No need to be feared just pick up the phone and call</div>
<div class="abs faq__item" style="top:2498px">What is your typical process for working with a new customer?<svg width="12" height="8"><path d="M0 0h12L6 7z" fill="#555"/></svg></div>
<div class="abs faq__item" style="top:2554px">What education and/or training do you have that relates to your work?<svg width="12" height="8"><path d="M0 0h12L6 7z" fill="#555"/></svg></div>
<div class="abs faq__item" style="top:2610px">How did you get started doing this type of work?<svg width="12" height="8"><path d="M0 0h12L6 7z" fill="#555"/></svg></div>
<div class="abs faq__item" style="top:2665px">What types of customers have you worked with?<svg width="12" height="8"><path d="M0 0h12L6 7z" fill="#555"/></svg></div>
<div class="abs faq__item" style="top:2721px">What advice would you give a customer looking to hire a provider in your area of work?<svg width="12" height="8"><path d="M0 0h12L6 7z" fill="#555"/></svg></div>
<div class="abs faq__item" style="top:2777px">What questions should customers think through before talking to professionals about their project?<svg width="12" height="8"><path d="M0 0h12L6 7z" fill="#555"/></svg></div>

<svg class="abs" style="top:2905px;left:0" width="1200" height="930" viewBox="0 2905 1200 930">
  <polygon points="0,3029 600,2907 1200,3029 1200,3831 600,3716 0,3831" fill="var(--grey)"/>
</svg>
<h2 class="abs heading gallery__title">Gallery</h2>
<div class="abs" role="img" aria-label="Shingles being installed on a roof" style="left:144px;top:3118px;width:218px;height:217px;background:linear-gradient(135deg,#7a6a55,#9aa0ac 60%,#6f7685)"></div>
<div class="abs" role="img" aria-label="Grey sided house with new roof decking" style="left:373px;top:3118px;width:454px;height:448px;background:linear-gradient(180deg,#5d88c4 0%,#6f9640 30%,#c78b3e 48%,#6f7c82 65%,#5a666c 100%)"></div>
<div class="abs" role="img" aria-label="Finished grey shingle roof" style="left:838px;top:3118px;width:218px;height:217px;background:linear-gradient(160deg,#9a9eaa,#6d7280)"></div>
<div class="abs" role="img" aria-label="Roof tear-off on a white house" style="left:144px;top:3349px;width:218px;height:217px;background:linear-gradient(180deg,#4e88c8 0%,#e6e6e2 40%,#7a6f5e 75%,#4d6b35)"></div>
<div class="abs" role="img" aria-label="New plywood roof decking" style="left:838px;top:3349px;width:218px;height:217px;background:linear-gradient(180deg,#d5b98e,#c7a673 85%,#222 100%)"></div>
<a class="btn" href="#" style="left:552px;top:3585px;width:96px;height:35px">READ MORE</a>

<div class="abs feature" style="left:291px">
  <svg width="34" height="32" viewBox="0 0 24 24"><path fill="#222" d="M2 10h4v12H2zM8 21V10l5-8c1.5 0 2.5 1 2.2 2.6L14.5 9H21c1.1 0 2 .9 2 2l-2.2 8.3c-.3.9-1 1.7-2 1.7z"/></svg>
  <div class="feature__text">Offering 30-50 year<br>warranties</div>
</div>
<div class="abs feature" style="left:600px">
  <svg width="38" height="32" viewBox="0 0 26 22"><rect x="1" y="1" width="24" height="20" rx="2" fill="none" stroke="#222" stroke-width="2.4"/><rect x="1" y="6" width="24" height="4" fill="#222"/><rect x="4" y="14" width="8" height="3" fill="#222"/></svg>
  <div class="feature__text">Accepting all major<br>credit cards, checks</div>
</div>
<div class="abs feature" style="left:908px">
  <svg width="38" height="34" viewBox="0 0 24 22"><path d="M12 1 23 21H1z" fill="#222"/><rect x="11" y="8" width="2" height="7" fill="#fff"/><rect x="11" y="16.5" width="2" height="2" fill="#fff"/></svg>
  <div class="feature__text">Checks Emergency services<br>available</div>
</div>

<footer>
  <svg class="abs" style="top:3990px;left:0" width="1200" height="229" viewBox="0 3990 1200 229">
    <polygon points="0,4109 600,3992 1200,4109 1200,4219 0,4219" fill="var(--dark)"/>
  </svg>
  <svg class="abs footer__social" viewBox="0 4046 1200 50" aria-label="Social media links">
    <g fill="none" stroke="#777" stroke-width="1.5">
      <polygon points="527,4043 552,4068 527,4093 502,4068"/>
      <polygon points="600,4043 625,4068 600,4093 575,4068"/>
      <polygon points="673,4043 698,4068 673,4093 648,4068"/>
    </g>
    <g fill="#888">
      <circle cx="527" cy="4068" r="6"/>
      <circle cx="600" cy="4068" r="6"/>
      <circle cx="673" cy="4068" r="6"/>
    </g>
  </svg>
  <nav class="abs footer__links">
    <a href="#">Home</a>|<a href="#">About Us</a>|<a href="#">Services</a>|<a href="#">Gallery</a>|<a href="#">Testimonials</a>|<a href="#">FAQ</a>|<a href="#">Contact Us</a>
  </nav>
  <p class="abs footer__copy">Copyright © 2019 Marlowe Restoration &amp; Remodeling Group, LLC. All rights reserved.</p>
</footer>

</body>
</html>
```